Children’s entertainer/balloon artist Website Home Page and custom landing page

I need a home page design for the home page of a children and family entertainer/balloon twister’s website. I also need a custom landing page for family theatre shows performed by the same entertainer.
It will be a Wordpress website and I need the final artwork in a layer Photoshop file with all the layers clearly named and labeled.

Target Market(s)

The site visitors are mainly mums, aged between early 20’s and late 30’s. Other visitors will included companies for Christmas functions, and event organisers for corporate functions.

Industry/Entity Type

Entertainment

Number of Pages Required

2 page

Font styles to use
Sans Serif

Colors
34a6d7
f37122

Requirements
Must have
• Layout
• I have included a wireframe for the home page layout and the custom landing page for your reference. This is a guide only and I welcome your interpretation with the rough layout provided.
• This website needs to look good on all devices as it will be fully responsive.
• It needs to include a footer area on the page, that has social media and a call to action area included.
• Colours
• The main colours for the site is:
• orange (call to action colour)
• ff6800
• blue/turquoise
• 42abc3
• Pictures
• I have included images of the entertainer/balloon artist for you to use/take inspiration from.
• These images will be included on the website. I want to show lots of people having fun.
• I would like to have elements of the logo used in isolation across the website
• i.e. the octopus figure to be included in the footer or the bird element to be included in the testimonial slider etc.
• Elements to include
• Note: use the images of the entertainer in the boxes on the home page (balloon shows, balloon twisting, balloon workshops, theatre shows (the three little balloon pigs on his head)
Nice to have
Should not have
• Element to avoid
• Stock imagery of balloon sculptures - use images provided.

```html
<!DOCTYPE html>
<html lang="en">
<head>
<meta charset="utf-8">
<title>Benny Hollister – Family Entertainer</title>
<link href="https://fonts.googleapis.com/css2?family=Fredoka:wght@500;600&family=Open+Sans:wght@400;600&display=swap" rel="stylesheet">
<style>
:root{
  --blue:#34a6d7;
  --blue-dark:#1f86b8;
  --blue-light:#7fd0f0;
  --orange:#f37122;
  --orange-dark:#d95a10;
  --yellow:#ffd23a;
  --ink:#555e66;
  --page:#eaf5fb;
  --white:#ffffff;
}
*{box-sizing:border-box;margin:0;padding:0}
html,body{width:784px;height:1200px;overflow:hidden;background:var(--page)}
body{font-family:"Open Sans",sans-serif;color:var(--ink)}
.canvas{position:relative;width:784px;height:1200px;overflow:hidden;background:var(--page)}
.head-bg{position:absolute;left:0;top:0;width:784px;height:230px;background:radial-gradient(circle at 50% 20%,var(--blue-light),var(--blue) 45%,var(--blue-dark))}
.head-wave{position:absolute;left:0;top:150px;width:784px;height:90px}
.brand{position:absolute;top:22px;left:0;width:784px;text-align:center;font-family:"Fredoka",sans-serif;font-weight:600;font-size:34px;color:var(--white)}
.brand .dot{display:inline-block;width:16px;height:16px;background:var(--yellow);border-radius:50%;margin-right:10px;vertical-align:middle}
.nav{position:absolute;top:160px;left:110px;width:564px;display:flex;justify-content:space-between;align-items:center}
.nav a{font-family:"Fredoka",sans-serif;font-weight:500;font-size:13px;color:var(--white);text-decoration:none;padding:5px 10px}
.nav a.current{border:2px solid var(--white);border-radius:16px}
.panel{position:absolute;left:95px;top:200px;width:600px;height:892px;background:var(--white)}
.hero{position:absolute;left:105px;top:208px;width:580px;height:288px;background:linear-gradient(120deg,#2c4f86,#3a7fc0 55%,#1d3560);overflow:hidden}
.hero-photo{position:absolute;left:0;top:0;width:330px;height:288px;background:radial-gradient(circle at 45% 50%,#e8a34a,#c0532f 35%,#3b79c2 70%,transparent)}
.hero-copy{position:absolute;right:24px;top:72px;width:220px;text-align:right}
.hero-copy h1{font-family:"Fredoka",sans-serif;font-weight:600;font-size:28px;color:var(--orange)}
.hero-copy p{font-size:11px;color:var(--white);margin:6px 0 14px;line-height:1.4;font-style:italic}
.btn{display:inline-block;background:var(--orange);color:var(--white);font-size:10px;font-weight:600;padding:6px 14px;border-radius:14px}
.dots{position:absolute;right:40px;bottom:14px;display:flex;gap:5px}
.dots i{width:7px;height:7px;border-radius:50%;background:var(--white);opacity:.5}
.dots i.on{opacity:1}
.testimonial{position:absolute;left:105px;top:510px;width:415px;height:118px;border:1px solid #e2e6e9;padding:10px 14px}
.testimonial h2,.section-title{font-family:"Fredoka",sans-serif;font-weight:500;font-size:14px;color:var(--blue)}
.testimonial p{font-size:9.5px;font-style:italic;line-height:1.5;margin-top:6px}
.testimonial .who{color:var(--orange);font-style:normal;font-weight:600}
.arrows{position:absolute;right:12px;top:12px;display:flex;gap:3px}
.arrows i{width:12px;height:12px;background:var(--orange);border-radius:2px}
.cta{position:absolute;left:535px;top:510px;width:150px;height:118px;background:var(--blue);color:var(--white);text-align:center;padding-top:12px}
.cta small{font-size:10px;display:block}
.cta strong{font-family:"Fredoka",sans-serif;font-size:17px;font-weight:500;display:block}
.cta .phone{font-size:15px;font-weight:600;margin:4px 0 8px;display:block}
.cta .btn{background:transparent;border:1px solid var(--white)}
.welcome-title{position:absolute;left:105px;top:646px}
.welcome-img{position:absolute;left:105px;top:672px;width:235px;height:168px;background:linear-gradient(135deg,#f6b8c8,#e87a9a 50%,#7a5a50)}
.welcome-copy{position:absolute;left:355px;top:672px;width:165px}
.welcome-copy .lead{font-family:"Fredoka",sans-serif;font-weight:500;font-size:11px;color:var(--orange);line-height:1.35}
.welcome-copy p{font-size:8px;line-height:1.45;margin-top:6px}
.welcome-copy .btn{margin-top:6px;background:var(--blue);font-size:8px;padding:4px 10px}
.news{position:absolute;left:535px;top:642px;width:150px}
.news ul{list-style:none;margin-top:8px}
.news li{display:flex;gap:8px;padding:6px 0;border-bottom:1px solid #e8ebee;font-size:8.5px;line-height:1.35}
.news .thumb{flex:none;width:30px;height:26px;background:linear-gradient(135deg,var(--blue-light),var(--orange))}
.boxes{position:absolute;left:105px;top:874px;width:580px;display:flex;gap:12px}
.box{width:136px;height:204px;background:var(--blue);color:var(--white);display:flex;flex-direction:column}
.box h3{font-family:"Fredoka",sans-serif;font-weight:500;font-size:12.5px;color:var(--yellow);padding:8px 10px;white-space:nowrap}
.box .img{height:92px;margin:0 6px;flex:none}
.box p{font-size:8px;line-height:1.45;padding:7px 10px 6px}
.box .btn{margin-left:10px;font-size:8px;padding:4px 10px;align-self:flex-start}
.footer-wave{position:absolute;left:0;top:1094px;width:784px;height:106px}
.social{position:absolute;top:1130px;left:0;width:784px;display:flex;justify-content:center;gap:8px}
.social i{width:16px;height:16px;border-radius:50%;border:1.5px solid var(--white)}
.footer-links{position:absolute;top:1156px;width:784px;text-align:center;font-size:8.5px;color:var(--white)}
.copy{position:absolute;top:1174px;width:784px;text-align:center;font-size:7.5px;color:var(--white);opacity:.85}
</style>
</head>
<body>
<div class="canvas">
  <div class="head-bg"></div>
  <svg class="head-wave" viewBox="0 0 784 90" preserveAspectRatio="none"><path d="M0 40 Q392 -10 784 40 L784 90 L0 90Z" fill="var(--page)"/><path d="M0 10 Q392 -25 784 10 L784 50 Q392 20 0 50Z" fill="var(--orange)"/></svg>
  <div class="brand"><span class="dot"></span>Benny Hollister</div>
  <nav class="nav">
    <a class="current">Home</a><a>Balloon Shows</a><a>Balloon Twisting</a><a>Theatre</a><a>Reviews</a><a>Contact</a>
  </nav>

  <div class="panel"></div>

  <section class="hero">
    <div class="hero-photo" role="img" aria-label="Entertainer wearing a colourful balloon hat"></div>
    <div class="hero-copy">
      <h1>Benny Hollister</h1>
      <p>Fun balloon magic and laughter for every party and family event</p>
      <span class="btn">Read More</span>
    </div>
    <div class="dots"><i class="on"></i><i></i><i></i><i></i></div>
  </section>

  <section class="testimonial">
    <h2>Testimonial</h2>
    <div class="arrows"><i></i><i></i></div>
    <p>“Benny made our daughter's birthday unforgettable. The kids laughed all afternoon and went home with amazing balloon animals. Highly recommended for any family party.”</p>
    <p class="who">Sarah Mills, Leeds</p>
  </section>

  <aside class="cta">
    <small>For any enquiries</small>
    <strong>Call Us Today</strong>
    <span class="phone">555-214-0837</span>
    <span class="btn">Get Started now</span>
  </aside>

  <h2 class="section-title welcome-title">Welcome to Benny Hollister</h2>
  <div class="welcome-img" role="img" aria-label="Entertainer with three balloon pigs on his head"></div>
  <div class="welcome-copy">
    <div class="lead">Bringing smiles, giggles and colourful balloon creations to parties, schools and events.</div>
    <p>Benny is a family entertainer and balloon artist who turns every celebration into a bright, joyful show for kids and grown ups alike.</p>
    <p>From birthday parties to corporate functions, each show is packed with comedy, music and giant balloon surprises.</p>
    <span class="btn">Read More</span>
  </div>

  <aside class="news">
    <h2 class="section-title">Latest News</h2>
    <ul>
      <li><span class="thumb" role="img" aria-label="News photo"></span>New family theatre show opens this spring</li>
      <li><span class="thumb" role="img" aria-label="News photo"></span>Balloon workshops now booking for schools</li>
      <li><span class="thumb" role="img" aria-label="News photo"></span>Christmas party dates filling up fast</li>
      <li><span class="thumb" role="img" aria-label="News photo"></span>Behind the scenes at a giant balloon build</li>
    </ul>
  </aside>

  <section class="boxes">
    <article class="box"><h3>Balloon Shows</h3><div class="img" role="img" aria-label="Child enjoying a balloon show" style="background:linear-gradient(135deg,#f7d36b,#e9893f)"></div><p>Lively balloon shows packed with fun for every birthday party.</p><span class="btn">Read More</span></article>
    <article class="box"><h3>Balloon Twisting</h3><div class="img" role="img" aria-label="Balloon twisting at a party" style="background:linear-gradient(135deg,#ffe066,#f5a623)"></div><p>Amazing balloon animals twisted live for every happy guest.</p><span class="btn">Read More</span></article>
    <article class="box"><h3>Balloon Workshops</h3><div class="img" role="img" aria-label="Children at a balloon workshop" style="background:linear-gradient(135deg,#e85b5b,#f2a04a)"></div><p>Hands-on workshops where kids learn to make their own creations.</p><span class="btn">Read More</span></article>
    <article class="box"><h3>Theatre Shows</h3><div class="img" role="img" aria-label="Family audience at a theatre show" style="background:linear-gradient(135deg,#f3c0c8,#e08a5a)"></div><p>Family theatre shows full of stories, songs and big balloon fun.</p><span class="btn">Read More</span></article>
  </section>

  <svg class="footer-wave" viewBox="0 0 784 106" preserveAspectRatio="none"><path d="M0 20 Q392 -12 784 20 L784 106 L0 106Z" fill="var(--orange)"/><path d="M0 26 Q392 -2 784 26 L784 38 Q392 10 0 38Z" fill="var(--blue)"/></svg>
  <div class="social"><i></i><i></i><i></i><i></i></div>
  <div class="footer-links">Home | Balloon Shows | Balloon Twisting | Theatre | Reviews | Contact</div>
  <div class="copy">© 2024 Benny Hollister. All rights reserved.</div>
</div>
</body>
</html>
```